International Perfume distribution Company needs a stationary design

We are a perfume development and distribution company named GLINTO and based in Sao Paulo Brazil. Basically we licence brazilian and international brands and celebrities to develop and distribute its fragrances and perfumes in Brazil. Our current licenced brands are: Varn Colter, Ravena, Delmor Viqueta fragrances and Lara Monteiro (brazilian soap opera celebrity).

We already have our logo and brand that reflects our massive distribution power in Brazil ("spraying our products accross Brazil") and we are also a branch of a big distribution company named BROMAX. It would be nice to mention it in our stationary ("uma divisao do grupo Bromax").

Industry/Entity Type

It Company

Requirements
Must have
• mention that Glinto is a division/branch of bromax using the following phrase: "uma divisão do grupo Bromax"

Use the logo signature: international fragrances

```html
<!DOCTYPE html>
<html lang="pt-BR">
<head>
<meta charset="utf-8">
<title>Glinto – Business Card</title>
<link href="https://fonts.googleapis.com/css2?family=Quicksand:wght@300;400;500;700&display=swap" rel="stylesheet">
<style>
  :root {
    --backdrop: #4b4b4d;
    --brand-purple: #35276f;
    --brand-purple-deep: #2b1f5e;
    --brand-orange: #e59a12;
    --veil: rgba(255, 255, 255, 0.32);
    --paper: #f4f4f3;
    --paper-band: #dcdcdc;
    --ink: #4a4a4a;
    --ink-soft: #5c5c5c;
    --white: #ffffff;
    --white-soft: rgba(255, 255, 255, 0.72);
  }
  * { box-sizing: border-box; margin: 0; padding: 0; }
  html, body {
    width: 1200px;
    height: 1000px;
    overflow: hidden;
    background: var(--backdrop);
    font-family: "Quicksand", sans-serif;
  }
  .stage { position: relative; width: 1200px; height: 1000px; }

  .card { position: absolute; width: 531px; height: 303px; overflow: hidden; }

  /* Front */
  .card--front {
    left: 206px; top: 164px;
    background: linear-gradient(180deg, var(--brand-purple) 0%, var(--brand-purple-deep) 100%);
  }
  .front__accent-bar {
    position: absolute; left: 349px; top: 0; width: 182px; height: 13px;
    background: var(--brand-orange);
  }
  .front__veil-block {
    position: absolute; left: 425px; top: 16px; width: 106px; height: 23px;
    background: var(--veil);
  }
  .front__side-tab {
    position: absolute; left: 0; top: 176px; width: 14px; height: 55px;
    background: var(--veil);
  }
  .brand { position: absolute; left: 90px; top: 177px; display: flex; align-items: center; }
  .brand__dot {
    width: 46px; height: 46px; border-radius: 50%;
    background: var(--brand-orange);
    margin-right: 34px;
  }
  .brand__text { color: var(--white); }
  .brand__name {
    font-weight: 300; font-size: 46px; line-height: 1; letter-spacing: 0.5px;
  }
  .brand__tagline {
    font-weight: 400; font-size: 11px; margin-top: 4px; margin-left: 3px;
  }
  .front__division {
    position: absolute; left: 173px; top: 270px;
    font-size: 10px; font-weight: 400; letter-spacing: 0.3px;
    color: var(--white-soft);
  }

  /* Back */
  .card--back {
    left: 472px; top: 549px;
    background: var(--paper);
  }
  .back__band {
    position: absolute; left: 259px; top: 0; width: 220px; height: 13px;
    background: var(--paper-band);
  }
  .back__address {
    position: absolute; right: 58px; top: 29px;
    text-align: right; color: var(--ink-soft); font-style: normal;
    font-size: 14px; line-height: 18.5px; font-weight: 400;
  }
  .person { position: absolute; left: 40px; top: 153px; }
  .person__name {
    font-size: 20px; font-weight: 400; color: var(--ink); letter-spacing: 0.5px;
  }
  .person__role { font-size: 14px; color: var(--ink-soft); margin-top: 1px; }
  .contact { position: absolute; left: 40px; top: 223px; font-size: 14px; line-height: 19px; color: var(--ink-soft); }
  .contact__label { display: inline-block; width: 16px; font-weight: 700; color: var(--brand-purple-deep); }
  .back__web {
    position: absolute; right: 58px; top: 242px;
    font-size: 14px; color: var(--ink-soft);
  }
  .back__web strong { color: var(--brand-purple-deep); font-weight: 700; font-size: 15px; }
  .back__marker {
    position: absolute; right: 0; top: 237px; width: 22px; height: 27px;
    background: var(--brand-purple-deep);
  }
</style>
</head>
<body>
<main class="stage">
  <section class="card card--front" aria-label="Card front">
    <div class="front__accent-bar"></div>
    <div class="front__veil-block"></div>
    <div class="front__side-tab"></div>
    <div class="brand">
      <span class="brand__dot"></span>
      <div class="brand__text">
        <div class="brand__name">GLINTO</div>
        <div class="brand__tagline">international fragrances</div>
      </div>
    </div>
    <div class="front__division">uma divisão do grupo Bromax</div>
  </section>

  <section class="card card--back" aria-label="Card back">
    <div class="back__band"></div>
    <address class="back__address">
      Rua das Acácias<br>
      n° 148, CEP 13041-520<br>
      Valinhos - São Paulo, Brasil
    </address>
    <div class="person">
      <div class="person__name">RAFAEL TAVARES</div>
      <div class="person__role">Managing director</div>
    </div>
    <div class="contact">
      <div><span class="contact__label">M</span> +55-19-3847-2610</div>
      <div><span class="contact__label">E</span> contato@glinto.com.br</div>
    </div>
    <div class="back__web">www.<strong>glinto</strong>.com.br</div>
    <div class="back__marker"></div>
  </section>
</main>
</body>
</html>
```